Consultant Firm Marketing Flyer

I want to use this flyer to market health care consultant services. I would like a front and back glossy, professional, yet bold and eye catching design. I would like it to convey knowledge, expertise, partnership and strength. The colors should blue and white but I am very open to the designer being creative. You can visit my website to see colors and images I want to use at brightharborcare.net
I would like the home page image on my website to be incorporated into the flyer but I am also open to other images that work with the design. The designer can be creative.

I want to highlight 4 service area’s of focus to my clients:
1. Revenue Cycle Optimization (making my clients money)
2. Practice Management Optimization (improving clinical operations)
3. Health Compliance (following the law)
4. Health Care Technology: (Telemedicine and AI)
Please be creative. Go where ever your creativity leads.

```html
<!DOCTYPE html>
<html lang="en">
<head>
<meta charset="utf-8">
<title>Bright Harbor Care – Flyer</title>
<link href="https://fonts.googleapis.com/css2?family=Montserrat:wght@400;500;600;700;800&display=swap" rel="stylesheet">
<style>
  :root {
    --navy: #1253a4;
    --blue: #1a6dc0;
    --sky: #5bb8e2;
    --ink: #1d1d1f;
    --white: #ffffff;
    --backdrop: #7b7571;
    --photo-a: #d9d6d2;
    --photo-b: #a98d7c;
    --desk-a: #eef0f3;
    --desk-b: #c9ced6;
  }
  * { margin: 0; padding: 0; box-sizing: border-box; }
  html, body { width: 1200px; height: 720px; overflow: hidden; }
  body { background: var(--backdrop); font-family: "Montserrat", Arial, sans-serif; color: var(--ink); position: relative; }

  .page { position: absolute; top: 30px; width: 510px; height: 660px; background: var(--white); overflow: hidden; }
  .page--front { left: 67px; }
  .page--back { left: 595px; }
  .page__art { position: absolute; inset: 0; }

  /* Front */
  .headline { position: absolute; left: 28px; top: 68px; color: var(--white); font-weight: 800; font-size: 31px; line-height: 36px; letter-spacing: 0.3px; }
  .brand { position: absolute; left: 29px; top: 262px; display: flex; align-items: center; gap: 10px; }
  .brand__dot { width: 30px; height: 30px; border-radius: 50%; background: var(--blue); }
  .brand__name { font-weight: 700; font-size: 17px; color: var(--navy); letter-spacing: 0.6px; }
  .welcome { position: absolute; left: 29px; top: 336px; width: 454px; }
  .welcome__kicker { color: var(--blue); font-weight: 500; font-size: 13px; letter-spacing: 0.3px; }
  .welcome__title { color: var(--navy); font-weight: 800; font-size: 16px; margin-top: 4px; }
  .welcome__body { margin-top: 9px; font-size: 9.6px; line-height: 11.55px; text-align: justify; }
  .contact { position: absolute; left: 19px; top: 578px; color: var(--white); }
  .contact__phone { display: flex; align-items: center; gap: 7px; font-weight: 700; font-size: 22px; }
  .contact__row { display: flex; gap: 44px; margin-top: 9px; margin-left: 6px; font-size: 10px; }
  .contact__item { display: flex; align-items: center; gap: 6px; }
  .contact__address { margin-left: 6px; margin-top: 3px; font-size: 10px; display: flex; align-items: center; gap: 6px; }

  /* Back */
  .focus-bar { position: absolute; left: 0; top: 262px; width: 510px; height: 54px; }
  .focus { position: absolute; top: 0; display: flex; align-items: center; gap: 8px; color: var(--white); }
  .focus__icon { width: 46px; height: 46px; border-radius: 50%; background: var(--white); display: flex; align-items: center; justify-content: center; flex-shrink: 0; }
  .focus__title { font-weight: 600; font-size: 8.4px; line-height: 10px; }
  .focus__note { font-size: 7.4px; line-height: 9.4px; }

  .services { position: absolute; left: 0; top: 0; width: 510px; height: 660px; }
  .service { position: absolute; }
  .service__title { color: var(--navy); font-weight: 600; font-size: 11.4px; line-height: 13.5px; letter-spacing: 0.1px; }
  .service__list { list-style: none; margin-top: 2px; }
  .service__list li { position: relative; padding-left: 9px; font-size: 8.3px; line-height: 12.5px; }
  .service__list li::before { content: "·"; position: absolute; left: 0; top: 0; font-weight: 700; }
  .service__list li.wrap { line-height: 10px; margin: 1px 0 2px; }
  .divider-v { position: absolute; left: 255px; top: 344px; width: 1px; height: 294px; background: var(--ink); }
  .divider-h { position: absolute; left: 19px; top: 475px; width: 491px; height: 1px; background: var(--ink); }
</style>
</head>
<body>

<!-- FRONT PAGE -->
<section class="page page--front">
  <svg class="page__art" viewBox="0 0 510 660" width="510" height="660">
    <defs>
      <linearGradient id="front-photo" x1="0" y1="0" x2="1" y2="1">
        <stop offset="0" stop-color="var(--photo-a)"/>
        <stop offset="1" stop-color="var(--photo-b)"/>
      </linearGradient>
      <linearGradient id="front-blue" x1="0" y1="0" x2="1" y2="1">
        <stop offset="0" stop-color="#1459ad"/>
        <stop offset="1" stop-color="#2a8fd6"/>
      </linearGradient>
    </defs>
    <rect width="510" height="400" fill="url(#front-blue)"/>
    <path d="M195 0 H510 V290 C420 275 330 230 275 170 C235 125 210 70 195 0 Z" fill="url(#front-photo)" role="img" aria-label="Photo of four healthcare professionals meeting around a table"/>
    <path d="M0 215 C130 190 320 200 440 280 C470 300 495 330 510 350 V400 C490 360 460 330 420 300 C300 215 120 200 0 240 Z" fill="var(--sky)"/>
    <path d="M0 240 C120 200 300 215 420 300 C460 330 490 360 510 400 V660 H0 Z" fill="var(--white)"/>
    <path d="M0 555 C180 540 360 560 510 600 V660 H0 Z" fill="var(--sky)"/>
    <path d="M0 572 C180 562 360 582 510 626 V660 H0 Z" fill="var(--navy)"/>
    <path d="M320 660 C420 645 480 628 510 618 V660 Z" fill="var(--sky)"/>
  </svg>

  <h1 class="headline">ADVANCING<br>HEALTHCARE<br>OPERATIONS</h1>

  <div class="brand">
    <span class="brand__dot"></span>
    <span class="brand__name">BRIGHT HARBOR CARE LLC</span>
  </div>

  <div class="welcome">
    <p class="welcome__kicker">WELCOME TO</p>
    <h2 class="welcome__title">BRIGHT HARBOR CARE</h2>
    <p class="welcome__body">Bright Harbor Care (BHC), founded in 2015, is a healthcare consulting firm skilled at helping physician practices advance their strategic vision in an ever-evolving healthcare system. Bright Harbor Care specializes in revenue cycle optimization, practice management improvement and developing new physician practices. Our technical skills allow us to dig deep into your revenue cycle while our strategic approach ensures we're keeping our eyes on the entire financial picture. By implementing a comprehensive approach to optimization and working closely with your people, processes, and technology, we develop a complete picture of your organization's performance. More importantly, we're able to design strategies and solutions that improve this performance while also preserving your organization's mission, vision, and strategic initiatives.</p>
  </div>

  <div class="contact">
    <p class="contact__phone">
      <svg width="24" height="20" viewBox="0 0 24 20" aria-hidden="true"><path d="M2 6 C2 2 22 2 22 6 L19 8 L16 6 V4 H8 V6 L5 8 Z" fill="var(--white)"/><rect x="5" y="9" width="14" height="9" rx="2" fill="var(--white)"/><circle cx="12" cy="13.5" r="2.5" fill="var(--navy)"/></svg>
      (555) 214-0387
    </p>
    <div class="contact__row">
      <span class="contact__item"><svg width="9" height="7" viewBox="0 0 9 7" aria-hidden="true"><rect width="9" height="7" fill="var(--white)"/><path d="M0 0 L4.5 4 L9 0" stroke="var(--navy)" fill="none"/></svg>info@brightharborcare.net</span>
      <span class="contact__item"><svg width="9" height="9" viewBox="0 0 9 9" aria-hidden="true"><circle cx="4.5" cy="4.5" r="4" fill="none" stroke="var(--white)"/><path d="M0.5 4.5 H8.5 M4.5 0.5 V8.5" stroke="var(--white)"/></svg>www.brightharborcare.net</span>
    </div>
    <p class="contact__address"><svg width="9" height="10" viewBox="0 0 9 10" aria-hidden="true"><path d="M4.5 10 C1 6 0.5 5 0.5 4 A4 4 0 0 1 8.5 4 C8.5 5 8 6 4.5 10 Z" fill="var(--white)"/><circle cx="4.5" cy="4" r="1.5" fill="var(--navy)"/></svg>118 Harbor Lane, Portsmouth, NH 03801, USA</p>
  </div>
</section>

<!-- BACK PAGE -->
<section class="page page--back">
  <svg class="page__art" viewBox="0 0 510 660" width="510" height="660">
    <defs>
      <linearGradient id="back-photo" x1="0" y1="0" x2="1" y2="1">
        <stop offset="0" stop-color="var(--desk-a)"/>
        <stop offset="1" stop-color="var(--desk-b)"/>
      </linearGradient>
    </defs>
    <path d="M0 0 H510 V268 C350 240 150 240 0 258 Z" fill="url(#back-photo)" role="img" aria-label="Photo of a laptop, calculator and stethoscope on a desk"/>
    <path d="M0 250 C150 232 350 232 510 262 V280 C350 250 150 250 0 268 Z" fill="var(--sky)"/>
    <path d="M0 262 C150 246 350 248 510 278 V328 H0 Z" fill="var(--navy)"/>
    <path d="M510 530 C480 600 420 648 300 660 H510 Z" fill="var(--sky)"/>
  </svg>

  <div class="focus-bar">
    <div class="focus" style="left:15px; top:10px;">
      <span class="focus__icon"><svg width="26" height="26" viewBox="0 0 26 26" aria-hidden="true" fill="none" stroke="var(--navy)" stroke-width="1.6"><path d="M13 3 L18 11 H8 Z"/><path d="M4 21 L8 13 L12 21 Z"/><path d="M14 21 H22 L18 13"/></svg></span>
      <div><p class="focus__title">Revenue Cycle<br>Optimization</p><p class="focus__note">(making my clients<br>money)</p></div>
    </div>
    <div class="focus" style="left:140px; top:10px;">
      <span class="focus__icon"><svg width="24" height="26" viewBox="0 0 24 26" aria-hidden="true" fill="none" stroke="var(--navy)" stroke-width="1.6"><rect x="4" y="3" width="16" height="21" rx="2"/><rect x="9" y="1" width="6" height="4" rx="1"/><path d="M7 11 l2 2 l3-3 M7 18 l2 2 l3-3 M14 12 H17 M14 19 H17"/></svg></span>
      <div><p class="focus__title">Practice Management<br>Optimization</p><p class="focus__note">(improving clinical<br>operations)</p></div>
    </div>
    <div class="focus" style="left:288px; top:10px;">
      <span class="focus__icon"><svg width="26" height="26" viewBox="0 0 26 26" aria-hidden="true" fill="none" stroke="var(--navy)" stroke-width="1.6"><path d="M3 12 C3 18 7 22 11 23 M23 12 C23 18 19 22 15 23"/><path d="M13 17 C8 13 8 8 11 8 C12 8 13 9 13 10 C13 9 14 8 15 8 C18 8 18 13 13 17 Z"/></svg></span>
      <div><p class="focus__title">Health<br>Compliance</p><p class="focus__note">(following<br>the law)</p></div>
    </div>
    <div class="focus" style="left:395px; top:10px;">
      <span class="focus__icon"><svg width="26" height="24" viewBox="0 0 26 24" aria-hidden="true" fill="none" stroke="var(--navy)" stroke-width="1.6"><rect x="3" y="3" width="20" height="14" rx="1"/><path d="M9 21 H17 M13 17 V21"/><circle cx="13" cy="10" r="3"/></svg></span>
      <div><p class="focus__title">Health Care<br>Technology</p><p class="focus__note">(Telemedicine<br>and AI)</p></div>
    </div>
  </div>

  <div class="services">
    <div class="divider-v"></div>
    <div class="divider-h"></div>

    <div class="service" style="left:30px; top:343px; width:220px;">
      <h3 class="service__title">REVENUE CYCLE OPTIMIZATION</h3>
      <ul class="service__list">
        <li>Medical Billing &amp; Coding</li>
        <li>Documentation &amp; Coding Audit</li>
        <li>A/R Management</li>
        <li>Dedicated Remote Billing Manager</li>
        <li>Dedicated Phone Number for Patients to Call</li>
        <li>Revenue Cycle Training for Practice Staff</li>
        <li>Monthly Reports</li>
        <li>Patient Access Assessment &amp; Optimization</li>
      </ul>
    </div>

    <div class="service" style="left:287px; top:343px; width:200px;">
      <h3 class="service__title">PRACTICE MANAGEMENT<br>OPTIMIZATION</h3>
      <ul class="service__list">
        <li>Medical Coding Regulations</li>
        <li>False Claims Act</li>
        <li>HIPPA Privacy &amp; Security Rules</li>
        <li>Emergency Medical Treatment and Active<br>Labor Act (EMTALA)</li>
        <li>Stark Law &amp; Anti-Kickback Statue</li>
        <li class="wrap">Occupational Safety &amp; Health Administration Guidelines (OSHA)</li>
      </ul>
    </div>

    <div class="service" style="left:30px; top:481px; width:220px;">
      <h3 class="service__title">PRACTICE MANAGEMENT</h3>
      <ul class="service__list">
        <li>A dedicated HR Manager</li>
        <li>Development of HR Policies and Procedures</li>
        <li>Employer Coaching and Guidance</li>
        <li>Assistance with Onboarding &amp; Terminations</li>
        <li>Compensation Compliance</li>
        <li>Navigation of Complex Labor Laws</li>
        <li>Staff Training</li>
        <li>Staff Recruitment &amp; Talent Acquisition</li>
        <li>Pre-hire background checks</li>
        <li class="wrap">Compliance Services: Affirmative Action, Fair labor Standards Act (FLSA) Compliance audit, FMLA &amp; Much More.</li>
      </ul>
    </div>

    <div class="service" style="left:287px; top:481px; width:200px;">
      <h3 class="service__title">HEALTH COMPLIANCE</h3>
      <ul class="service__list">
        <li>Patient Access &amp; Scheduling</li>
        <li>Patient Experience</li>
        <li>Staff Experience</li>
        <li>Online Reputation Management</li>
        <li>Strategic Planning</li>
      </ul>
    </div>
  </div>
</section>

</body>
</html>
```